Newsletter Design for Financial Education Videos Startup

Brightpenny is an online resource for those who want to learn more about finance basics - including topics such as retirement, investing, taxes, credit score, savings, and much more! We provide structured online video courses that go into deeper topics such as accounting, calculating taxes, retirement strategies, CPA/CFA overview, etc.
We want a newsletter that really catches the eye and fits the financial-education-for-the-average-person business.
Our newsletter won't have too much content, it will include a video at the top, followed by 3 news headlines with 1-2 sentences explaining the relevance to our subscribers. I've included an example of a template that was created, but it is not at all necessary to stick to that layout - feel free to deviate as much as you want and be creative. Finance seems boring, and that's not us!!
As you can see, our logo is pretty colorful. I'm thinking the colors used for the newsletter should work well with the colors used in our logo (does not have to be the same colors but overall should feel coherent).
Newsletter must work on Mailchimp - HTML code will have to be provided for this.

```html
<!DOCTYPE html>
<html lang="en">
<head>
<meta charset="utf-8">
<title>Brightpenny Newsletter</title>
<link rel="stylesheet" href="https://fonts.googleapis.com/css2?family=Lato:ital,wght@0,400;0,700;0,900;1,400&display=swap">
<style>
  :root {
    --maroon: #8a0c46;
    --orange: #f0904c;
    --green: #bdcf86;
    --blue: #94c7e1;
    --grey-band: #d3d2d2;
    --white: #ffffff;
    --ink: #4a4a4a;
    --muted: #b9b9b9;
    --video-dark: #6f6a5c;
    --video-light: #b9b2a0;
  }
  * { box-sizing: border-box; margin: 0; padding: 0; }
  html, body {
    width: 688px; height: 1200px; overflow: hidden;
    background: var(--white);
    font-family: "Lato", Arial, sans-serif;
  }
  .newsletter { position: relative; width: 688px; height: 1200px; overflow: hidden; background: var(--white); }

  /* Header */
  .brand { position: absolute; top: 54px; left: 0; width: 100%; text-align: center; }
  .brand__mark { display: inline-flex; align-items: center; gap: 10px; }
  .brand__dot { width: 24px; height: 24px; border-radius: 50%; background: var(--maroon); }
  .brand__name { font-weight: 900; font-size: 32px; line-height: 40px; letter-spacing: 1px; color: var(--maroon); text-transform: uppercase; }

  /* Hero */
  .hero-bg { position: absolute; top: 126px; left: 0; width: 688px; height: 448px; }
  .hero__video {
    position: absolute; left: 150px; top: 170px; width: 387px; height: 214px;
    background: linear-gradient(135deg, var(--video-dark) 0%, var(--video-light) 45%, #8c8676 100%);
  }
  .hero__play { position: absolute; left: 166px; top: 75px; }
  .hero__title {
    position: absolute; top: 393px; left: 0; width: 100%; text-align: center;
    color: var(--white); font-weight: 700; font-size: 29px; line-height: 36px; letter-spacing: 3px;
  }
  .hero__rule { position: absolute; left: 235px; width: 206px; height: 1px; background: var(--white); }
  .hero__rule--top { top: 436px; }
  .hero__rule--bottom { top: 539px; }
  .hero__text {
    position: absolute; top: 450px; left: 0; width: 100%; text-align: center;
    color: var(--white); font-size: 18px; line-height: 23px; white-space: nowrap;
  }

  /* News items */
  .news { position: absolute; left: 0; width: 688px; height: 155px; }
  .news--orange { top: 573px; background: var(--orange); }
  .news--green { top: 728px; background: var(--green); }
  .news--blue { top: 883px; background: var(--blue); }
  .news__photo { position: absolute; top: 0; width: 197px; height: 155px; }
  .news__photo--left { left: 21px; }
  .news__photo--right { left: 470px; }
  .news__photo--car { background: linear-gradient(160deg, #3a3f55 0%, #7d8291 55%, #2a2c35 100%); }
  .news__photo--meeting { background: linear-gradient(120deg, #efe9e2 0%, #8a8680 50%, #2f3140 100%); }
  .news__photo--calculator { background: linear-gradient(150deg, #e8e6e3 0%, #b5b1ab 50%, #3b3a38 100%); }
  .news__body { position: absolute; top: 20px; color: var(--white); white-space: nowrap; }
  .news__body--right { left: 251px; }
  .news__body--left { left: 20px; }
  .news__title { font-weight: 900; font-size: 23px; line-height: 28px; margin-bottom: 2px; }
  .news__text { font-size: 18px; line-height: 23px; }

  /* Footer */
  .footer-bg { position: absolute; top: 1038px; left: 0; width: 688px; height: 162px; }
  .social { position: absolute; top: 1055px; left: 0; width: 100%; display: flex; justify-content: center; gap: 16px; }
  .social__item { width: 30px; height: 30px; background: var(--maroon); border-radius: 3px; }
  .copyright {
    position: absolute; top: 1093px; left: 0; width: 100%; text-align: center;
    color: var(--muted); font-size: 14px; line-height: 17px;
  }
  .site { position: absolute; top: 1151px; left: 0; width: 100%; text-align: center; color: var(--ink); font-weight: 700; font-size: 14px; }
  .fineprint {
    position: absolute; top: 1172px; left: 0; width: 100%; text-align: center;
    color: var(--ink); font-style: italic; font-size: 8px; line-height: 12px;
  }
  .fineprint a { color: var(--ink); }
</style>
</head>
<body>
<main class="newsletter">

  <header class="brand">
    <div class="brand__mark">
      <span class="brand__dot"></span>
      <span class="brand__name">Brightpenny</span>
    </div>
  </header>

  <svg class="hero-bg" viewBox="0 0 688 448" preserveAspectRatio="none" aria-hidden="true">
    <path d="M0 45 Q344 -30 688 45 L688 448 L0 448 Z" fill="var(--maroon)"/>
  </svg>

  <section class="hero">
    <div class="hero__video" role="img" aria-label="Video thumbnail: a rolled bundle of banknotes">
      <svg class="hero__play" width="56" height="64" viewBox="0 0 56 64" aria-hidden="true">
        <path d="M6 4 Q4 2 4 8 L4 56 Q4 62 9 59 L52 35 Q56 32 52 29 L9 5 Z" fill="#ffffff"/>
      </svg>
    </div>
    <h1 class="hero__title">MONEY WITH MARLOW</h1>
    <div class="hero__rule hero__rule--top"></div>
    <p class="hero__text">Lorem ipsum dolor sit amet, consectetur adipisic-<br>ing elit, sed do eiusmod tempor incididunt ut<br>labore et dolore magna aliqua. Ut enim ad minim</p>
    <div class="hero__rule hero__rule--bottom"></div>
  </section>

  <article class="news news--orange">
    <div class="news__photo news__photo--left news__photo--car" role="img" aria-label="Photo: a silver sports car at a launch event"></div>
    <div class="news__body news__body--right">
      <h2 class="news__title">NEWS TITLE</h2>
      <p class="news__text">Lorem ipsum dolor sit amet, consectetur adipisic-<br>ing elit, sed do eiusmod tempor incididunt ut<br>labore et dolore magna aliqua. Ut enim ad minim</p>
    </div>
  </article>

  <article class="news news--green">
    <div class="news__body news__body--left">
      <h2 class="news__title">NEWS TITLE</h2>
      <p class="news__text">Lorem ipsum dolor sit amet, consectetur adipisic-<br>ing elit, sed do eiusmod tempor incididunt ut<br>labore et dolore magna aliqua. Ut enim ad minim</p>
    </div>
    <div class="news__photo news__photo--right news__photo--meeting" role="img" aria-label="Photo: officials in suits seated at a meeting"></div>
  </article>

  <article class="news news--blue">
    <div class="news__photo news__photo--left news__photo--calculator" role="img" aria-label="Photo: a calculator and pen on financial papers"></div>
    <div class="news__body news__body--right">
      <h2 class="news__title">NEWS TITLE</h2>
      <p class="news__text">Lorem ipsum dolor sit amet, consectetur adipisic-<br>ing elit, sed do eiusmod tempor incididunt ut<br>labore et dolore magna aliqua. Ut enim ad minim</p>
    </div>
  </article>

  <svg class="footer-bg" viewBox="0 0 688 162" preserveAspectRatio="none" aria-hidden="true">
    <path d="M0 68 Q344 122 688 68 L688 162 L0 162 Z" fill="var(--grey-band)"/>
  </svg>

  <footer>
    <nav class="social" aria-label="Social links">
      <span class="social__item" role="img" aria-label="Social link 1"></span>
      <span class="social__item" role="img" aria-label="Social link 2"></span>
      <span class="social__item" role="img" aria-label="Social link 3"></span>
      <span class="social__item" role="img" aria-label="Social link 4"></span>
      <span class="social__item" role="img" aria-label="Social link 5"></span>
    </nav>
    <p class="copyright">Copyright © 2018, Brightpenny Learning Co.<br>All Rights Reserved.</p>
    <p class="site">www.brightpenny-learn.com</p>
    <p class="fineprint">You are receiving these emails because you are subscribed to our newsletters.<br>To update your preferences, <a href="#">click here</a>.</p>
  </footer>

</main>
</body>
</html>
```